I need a label with logo to go on jars of honey.
Label size 70mm x 70mm
The front label should say :
The Tall Fern Honey Co. (logo)
Tarepo Honey
400g
The back label:
Would have nutritional information
And our address
You can see from the uploaded files the styles I prefer, I have uploaded a photo of the honey product too. The background of the logo doesn't have to be white. I would like to develop a color scheme that would look nice against the color of the honey.
Logo Text
The Tall Fern Honey Co. / The Tall Fern Honey Company

```html
<!DOCTYPE html>
<html lang="en">
<head>
<meta charset="utf-8">
<title>Tarepo Honey – Jar Labels</title>
<link rel="stylesheet" href="https://fonts.googleapis.com/css2?family=Kaushan+Script&family=Roboto:wght@400;700&family=Roboto+Condensed:wght@400;700&family=Dancing+Script:wght@700&display=swap">
<style>
  :root {
    --page: #ffffff;
    --label-edge: #f39a1e;
    --label-cream: #fdf0d8;
    --label-cream-deep: #f9dfae;
    --band-brown: #5a3418;
    --honey-orange: #f7a21c;
    --ink: #1d1d1d;
    --badge-dark: #3d3f42;
    --white: #ffffff;
  }
  * { box-sizing: border-box; margin: 0; padding: 0; }
  html, body { width: 1000px; height: 1200px; overflow: hidden; background: var(--page); }
  .sheet { position: relative; width: 1000px; height: 1200px; }

  .label {
    position: absolute;
    top: 420px;
    width: 455px;
    height: 410px;
    border: 5px solid var(--label-edge);
    border-radius: 26px;
    background: radial-gradient(circle at 50% 60%, var(--label-cream) 0%, var(--label-cream-deep) 100%);
    overflow: hidden;
  }
  .label--front { left: 28px; }
  .label--back { left: 517px; }

  .label__pattern {
    position: absolute; inset: 0;
    background: radial-gradient(circle at 50% 75%, rgba(255,255,255,0.55) 0%, rgba(255,255,255,0) 60%);
  }

  .band { position: absolute; left: 0; top: 0; width: 100%; height: 100%; }

  .brand-name {
    position: absolute;
    display: flex; align-items: center; gap: 8px;
    font-family: "Roboto Condensed", sans-serif;
    font-weight: 700;
    font-size: 19px;
    color: var(--badge-dark);
    background: var(--white);
    padding: 8px 14px;
    border-radius: 40px;
    z-index: 3;
    white-space: nowrap;
  }
  .brand-name__dot { width: 18px; height: 18px; border-radius: 50%; background: var(--badge-dark); }
  .brand-name--front { top: 388px; left: 140px; }
  .brand-name--back { top: 388px; left: 738px; }

  .product-title {
    position: absolute;
    font-family: "Kaushan Script", cursive;
    font-weight: 400;
    color: var(--honey-orange);
    line-height: 0.9;
    text-shadow: 2px 2px 0 var(--white), -1px -1px 0 var(--white), 3px 4px 4px rgba(0,0,0,0.35);
    transform: rotate(-9deg);
    transform-origin: left top;
    white-space: nowrap;
  }
  .product-title--front { left: 60px; top: 150px; font-size: 76px; }
  .product-title--front .product-title__line2 { display: block; padding-left: 80px; }
  .product-title--back { left: 16px; top: 36px; font-size: 40px; }
  .product-title--back .product-title__line2 { display: block; padding-left: 38px; }

  .seal {
    position: absolute;
    border-radius: 50%;
    background: radial-gradient(circle, #f4ece0 0%, #d9cbb6 70%, #8a7a66 100%);
    border: 3px solid var(--white);
  }
  .seal--front { left: 345px; top: 90px; width: 82px; height: 82px; }
  .seal--back { left: 165px; top: 14px; width: 44px; height: 44px; }

  .net-weight {
    position: absolute; right: 24px; bottom: 22px;
    font-family: "Roboto Condensed", sans-serif;
    font-weight: 700;
    font-size: 22px;
    color: var(--band-brown);
  }

  .bottler {
    position: absolute; left: 0; right: 0; bottom: 18px;
    text-align: center;
    font-family: "Dancing Script", cursive;
    color: var(--ink);
    line-height: 1.1;
  }
  .bottler__lead { font-size: 17px; }
  .bottler__name { font-size: 19px; }
  .bottler__note { font-size: 11px; }

  .nutrition {
    position: absolute; left: 75px; top: 106px; width: 300px;
    font-family: "Roboto Condensed", sans-serif;
    color: var(--ink);
  }
  .nutrition__heading {
    font-family: "Roboto", sans-serif;
    font-weight: 700;
    font-size: 15px;
    text-align: center;
    margin-bottom: 8px;
  }
  .nutrition__serving {
    background: var(--band-brown);
    color: var(--white);
    font-size: 13.5px;
    padding: 7px 8px;
    text-align: center;
  }
  .nutrition__table {
    width: 100%;
    border-collapse: collapse;
    background: var(--white);
    font-size: 13px;
    line-height: 1.2;
  }
  .nutrition__table th, .nutrition__table td {
    border: 1px solid var(--ink);
    text-align: left;
    vertical-align: top;
    padding: 6px 6px;
    font-weight: 400;
  }
  .nutrition__table th { height: 56px; }

  .address {
    position: absolute; left: 0; right: 0; bottom: 14px;
    text-align: center;
    font-family: "Roboto Condensed", sans-serif;
    font-size: 12px;
    line-height: 1.3;
    color: var(--ink);
  }
  .address__name { font-weight: 700; }
</style>
</head>
<body>
<main class="sheet">

  <section class="label label--front" aria-label="Front label">
    <div class="label__pattern" role="img" aria-label="Faint traditional Māori patterned background"></div>
    <svg class="band" viewBox="0 0 455 410" aria-hidden="true">
      <polygon points="0,150 455,38 455,140 270,205 0,280" fill="var(--band-brown)"/>
    </svg>
    <div class="seal seal--front" role="img" aria-label="Round Māori carved-mask emblem"></div>
    <h1 class="product-title product-title--front">Tarepo<span class="product-title__line2">Honey</span></h1>
    <p class="bottler">
      <span class="bottler__lead">Bottled by:</span><br>
      <span class="bottler__name">The Tall Fern Honey Co.</span><br>
      <span class="bottler__note">address or other company text</span>
    </p>
    <p class="net-weight">400g</p>
  </section>
  <div class="brand-name brand-name--front"><span class="brand-name__dot"></span>The Tall Fern Honey Co.</div>

  <section class="label label--back" aria-label="Back label">
    <div class="label__pattern" role="img" aria-label="Faint traditional Māori patterned background"></div>
    <svg class="band" viewBox="0 0 455 410" aria-hidden="true">
      <polygon points="0,20 280,0 260,55 0,110" fill="var(--band-brown)"/>
    </svg>
    <div class="seal seal--back" role="img" aria-label="Round Māori carved-mask emblem"></div>
    <h2 class="product-title product-title--back">Tarepo<span class="product-title__line2">Honey</span></h2>

    <div class="nutrition">
      <h3 class="nutrition__heading">NUTRITION INFORMATION</h3>
      <p class="nutrition__serving">Serving per package: 20 Serving Size: 20 g</p>
      <table class="nutrition__table">
        <tr>
          <th></th>
          <th>Average Quantity per Serving</th>
          <th>Average Quantity per 100g</th>
        </tr>
        <tr>
          <td>Energy<br>Protein<br>Fat, total<br>- Saturated<br>Carbohydrate<br>- Sugars<br>Sodium</td>
          <td>272 kJ<br>0.08 g<br>0 g<br>0 g<br>15.9 g<br>15.6 g<br>2.4 mg</td>
          <td>1360 kJ<br>0.4 g<br>0 g<br>0 g<br>79.6 g<br>78.1 g<br>12 mg</td>
        </tr>
      </table>
    </div>

    <address class="address">
      <span class="address__name">The Tall Fern Honey Company</span><br>
      14 Kowhai Ridge Road, Tarepo 3472, New Zealand
    </address>
  </section>
  <div class="brand-name brand-name--back"><span class="brand-name__dot"></span>The Tall Fern Honey Co.</div>

</main>
</body>
</html>
```